Startup company business card (Media & Advertising)

we need a business card design for a company that is a startup in the media and aggregation industry. Card needs to look funky and of a new breed/modern and upmarket.

Target Market(s)

advertisers/ brand agencies & media publishers

Industry/Entity Type

Advertising

Contact Information for Business Card

Please ensure the front face signifies our brand (plumvexo.com) and back has details for the contact. Standard contact such as phone , address, email , website etc.

Font styles to use
Other font styles liked:
• use styleguide and logo font and color

Colors

Designer to choose colors to be used in the design.

Requirements
Must have
• We are disrupting the media and agency industry so subtlety would be good to use imagery to signify this
Nice to have
• Please use logo colors for branding
Should not have
• be as creative and provide few options. Pick a brand color from logo and styleguide

```html
<!DOCTYPE html>
<html lang="en">
<head>
<meta charset="utf-8">
<title>plumvexo — Business Card</title>
<link rel="stylesheet" href="https://fonts.googleapis.com/css2?family=Montserrat:wght@400;500;700&display=swap">
<style>
  :root {
    --page-bg: #e9e6e3;
    --card-black: #0a0a0c;
    --card-black-soft: #16161a;
    --brand-red: #e8374f;
    --brand-red-deep: #b8203f;
    --text-white: #f4f4f4;
    --text-muted: #cfcfd3;
  }
  * { box-sizing: border-box; margin: 0; padding: 0; }
  html, body {
    width: 1200px; height: 909px; overflow: hidden;
    background: var(--page-bg);
    font-family: "Montserrat", Arial, sans-serif;
  }
  .sheet {
    width: 1200px; height: 909px;
    display: flex; flex-direction: column; align-items: center; justify-content: center;
    gap: 48px;
  }
  .card {
    position: relative;
    width: 620px; height: 354px;
    background: var(--card-black);
    border-bottom: 6px solid var(--brand-red);
    box-shadow: 0 10px 24px rgba(0,0,0,.25);
    overflow: hidden;
  }
  .card--front { margin-right: 260px; }
  .card--back { margin-left: 260px; }

  /* Front */
  .front-pattern {
    position: absolute; inset: 0;
    background: linear-gradient(135deg, var(--card-black-soft) 0%, var(--card-black) 70%);
  }
  .front-brand {
    position: absolute; right: 70px; top: 150px;
    display: flex; align-items: center; gap: 12px;
  }
  .brand-dot {
    width: 30px; height: 30px; border-radius: 50%;
    background: var(--brand-red);
  }
  .front-brand .brand-name {
    color: var(--brand-red);
    font-weight: 700; font-size: 30px; letter-spacing: .5px;
  }

  /* Back */
  .back-brand {
    position: absolute; left: 48px; top: 58px;
    display: flex; align-items: center; gap: 14px;
  }
  .back-brand .brand-dot { width: 40px; height: 40px; }
  .back-brand .brand-name {
    color: var(--text-white);
    font-weight: 700; font-size: 36px;
  }
  .person {
    position: absolute; right: 44px; top: 130px;
    text-align: right;
  }
  .person__name {
    color: var(--brand-red);
    font-weight: 700; font-size: 22px; letter-spacing: 2px;
    text-transform: uppercase;
  }
  .person__title {
    color: var(--text-white);
    font-size: 13px; margin-top: 2px; letter-spacing: .5px;
  }
  .divider {
    position: absolute; left: 48px; right: 44px; top: 194px;
    height: 1px; background: var(--brand-red-deep);
  }
  .address {
    position: absolute; left: 48px; top: 210px;
    color: var(--text-white); font-size: 14px; line-height: 1.35;
  }
  .contacts {
    position: absolute; left: 48px; top: 262px;
    list-style: none;
    color: var(--text-white); font-size: 14px; line-height: 1.5;
  }
  .contacts li { display: flex; align-items: center; gap: 9px; }
  .contacts svg { width: 12px; height: 12px; fill: var(--brand-red); flex: none; }
</style>
</head>
<body>
<main class="sheet">

  <section class="card card--front" aria-label="Card front">
    <div class="front-pattern" role="img" aria-label="Repeating faint brand-symbol pattern on black"></div>
    <div class="front-brand">
      <span class="brand-dot"></span>
      <span class="brand-name">plumvexo</span>
    </div>
  </section>

  <section class="card card--back" aria-label="Card back">
    <div class="back-brand">
      <span class="brand-dot"></span>
      <span class="brand-name">plumvexo</span>
    </div>

    <div class="person">
      <div class="person__name">Marten Hollis</div>
      <div class="person__title">General Manager</div>
    </div>

    <div class="divider"></div>

    <address class="address" style="font-style:normal">
      418 W Corvel Ave<br>
      Brenmoor County 40218
    </address>

    <ul class="contacts">
      <li>
        <svg viewBox="0 0 24 24" aria-hidden="true"><path d="M6.6 10.8a15.1 15.1 0 0 0 6.6 6.6l2.2-2.2a1 1 0 0 1 1-.25 11.4 11.4 0 0 0 3.6.6 1 1 0 0 1 1 1V20a1 1 0 0 1-1 1A17 17 0 0 1 3 4a1 1 0 0 1 1-1h3.5a1 1 0 0 1 1 1c0 1.25.2 2.45.6 3.6a1 1 0 0 1-.25 1z"/></svg>
        555-201-7730
      </li>
      <li>
        <svg viewBox="0 0 24 24" aria-hidden="true"><path d="M2 5h20v14H2z M2 5l10 8 10-8" /></svg>
        info@plumvexo.com
      </li>
      <li>
        <svg viewBox="0 0 24 24" aria-hidden="true"><circle cx="12" cy="12" r="10"/></svg>
        www.plumvexo.com
      </li>
    </ul>
  </section>

</main>
</body>
</html>
```